Sports Physical Therapy needs a New website look and update!

New updated look. Most people do not know they can go directly to a physical therapist for care. Cost effective and specialized. Getting back to your life and activity is what we do. What we treat. Your first cost effective provider for pain" for example. We treat children to seniors. Theme should be warm, caring, individualized, respect your time, and cost -effective. Mobile phone ready. Encourage taking action to call and schedule to get back to life, sports, activity.
Add link to send appointment request or contact us now
Add link ( code) for patients to fill out intake form or appointment request. I want to add testimonials for other therapists.
***My current website is "ferncliffpt.net"

Physical Therapy

```html
<!DOCTYPE html>
<html lang="en">
<head>
<meta charset="utf-8">
<title>Ferncliff Physical Therapy</title>
<link href="https://fonts.googleapis.com/css2?family=Libre+Baskerville:wght@400;700&family=Open+Sans:ital,wght@0,400;0,600;0,700;1,400&display=swap" rel="stylesheet">
<style>
:root{
  --teal:#0b7f97;
  --lime:#86c832;
  --ink:#333;
  --muted:#666;
  --soft:#f2f2f2;
  --footer:#333;
  --bar:#242424;
  --white:#fff;
}
*{margin:0;padding:0;box-sizing:border-box}
html,body{width:1200px;height:2985px;overflow:hidden}
body{position:relative;background:var(--white);font-family:"Open Sans",Arial,sans-serif;color:var(--ink)}
.abs{position:absolute}
a{text-decoration:none}
.serif{font-family:"Libre Baskerville",Georgia,serif;font-weight:700}
.btn{position:absolute;display:flex;align-items:center;justify-content:center;border-radius:16px;color:var(--white);font-size:12.5px;height:32px}
.btn-teal{background:var(--teal)}
.btn-lime{background:var(--lime)}

/* header */
.brand{position:absolute;left:132px;top:17px;display:flex;align-items:center;gap:8px}
.brand-dot{width:62px;height:62px;border-radius:50%;background:var(--teal)}
.brand-name{font-size:30px;font-weight:700;color:var(--teal);line-height:1}
.brand-name small{display:block;font-size:10px;letter-spacing:.8px;margin-top:2px}
.main-nav{position:absolute;left:426px;top:38px;display:flex;gap:22px;font-size:12.5px}
.main-nav a{color:var(--ink)}
.main-nav a.active{color:var(--lime);border-bottom:2px solid var(--lime);padding-bottom:5px}
.nav-book{left:918px;top:32px;width:152px}

/* hero */
.hero-photo{left:0;top:96px;width:1200px;height:400px;
  background:linear-gradient(100deg,#d8c8b8 0%,#f0ece6 10%,#e7d3bf 18%,#b9c7d6 28%,#eef1f3 36%,#c7a48a 46%,#2e3845 54%,#415063 60%,#d9dee2 68%,#a8b8c6 76%,#c3413c 84%,#2f56a0 90%,#d0d6dc 100%)}
.hero-panel{left:0;top:410px;width:818px;height:180px;background:var(--teal);color:var(--white)}
.hero-panel h1{position:absolute;left:158px;top:20px;font-size:25px;white-space:nowrap}
.hero-panel p{position:absolute;left:158px;top:58px;width:600px;font-size:15px;line-height:20px}
.hero-contact{left:158px;top:124px;width:128px}
.slider-arrows{position:absolute;display:flex;width:82px;height:32px}
.slider-arrows span{flex:1;display:flex;align-items:center;justify-content:center;color:#fff;font-size:15px;font-weight:700}
.slider-arrows span:first-child{background:var(--teal);border-radius:16px 0 0 16px}
.slider-arrows span:last-child{background:var(--lime);border-radius:0 16px 16px 0}

/* section headings */
.section-title{position:absolute;display:flex;align-items:center;height:60px;font-size:21px;color:var(--ink)}
.section-title svg{margin-right:6px}

/* about */
.about-text{left:158px;top:742px;width:484px;font-size:11.8px;line-height:16px;color:var(--muted)}
.about-text p+p{margin-top:16px}
.about-more{left:158px;top:932px;width:128px}
.about-collage{left:692px;top:636px;width:356px;height:356px;border-radius:50%;overflow:hidden;display:grid;grid-template-columns:1fr 1fr;grid-template-rows:1fr 1fr;gap:4px;background:#fff}
.about-collage div:nth-child(1){background:linear-gradient(160deg,#fbf3ea 0%,#f1d3b8 35%,#e3b28f 60%,#f6ece4 100%)}
.about-collage div:nth-child(2){background:linear-gradient(200deg,#6f7f8a 0%,#3f4e59 45%,#c8a34a 62%,#2f3a42 100%)}
.about-collage div:nth-child(3){background:linear-gradient(180deg,#e9e4de 0%,#cfc6bb 40%,#403a38 70%,#b7aca2 100%)}
.about-collage div:nth-child(4){background:linear-gradient(160deg,#d7e6f1 0%,#a9c6dc 35%,#e8d3c6 60%,#d86aa0 100%)}

/* services */
.services{left:0;top:1042px;width:1200px;height:392px;background:var(--soft)}
.services-intro{left:158px;top:154px;width:206px;font-size:11.8px;line-height:16px;color:var(--muted)}
.services-all{left:158px;top:280px;width:110px}
.service-card{position:absolute;top:48px;width:206px;height:294px;background:var(--white)}
.service-card .photo{height:162px}
.service-card h3{margin:10px 12px 5px;font-size:14px;font-weight:600}
.service-card p{margin:0 12px;font-size:11.8px;line-height:16px;color:var(--muted)}
.service-card a{display:block;margin:9px 12px 0;font-size:11.8px;font-weight:700;color:var(--teal)}
.service-card.active{box-shadow:0 2px 8px rgba(0,0,0,.18)}
.service-card.active a{color:var(--lime)}

/* providers */
.provider{position:absolute;top:1570px;width:180px;text-align:center}
.provider .avatar{width:152px;height:152px;margin:0 auto;border-radius:50%}
.provider.highlight .avatar{background:radial-gradient(circle at 50% 45%,#c4dc6e 0%,#9cc93b 60%,#86b52c 100%);display:flex;align-items:center;justify-content:center;gap:12px}
.provider.highlight .avatar i{width:10px;height:10px;border-radius:50%;background:#fff}
.provider h4{margin-top:26px;font-size:14.5px;font-weight:600;line-height:18px}
.provider span{font-size:11.5px;color:var(--muted)}
.providers-all{left:546px;top:1810px;width:112px}

/* testimonials */
.testimonials{left:0;top:1890px;width:1200px;height:450px;background:var(--soft)}
.video{left:158px;top:138px;width:356px;height:264px;background:linear-gradient(180deg,#6d6a66 0%,#4a4744 30%,#8a7566 55%,#5d5a57 80%,#3e3c3a 100%)}
.play{left:152px;top:106px;width:52px;height:52px}
.quote-mark{left:796px;top:154px}
.quote-text{left:590px;top:210px;width:462px;text-align:center;font-size:13.5px;line-height:19.5px;font-style:italic;color:var(--muted)}
.quote-name{left:590px;top:316px;width:462px;text-align:center;font-size:14.5px;font-weight:600}
.quote-role{left:590px;top:338px;width:462px;text-align:center;font-size:11.5px;color:var(--muted)}
.dots{left:810px;top:386px;display:flex;gap:5px}
.dots i{width:6px;height:6px;border-radius:50%;background:#bbb}
.dots i.on{background:var(--lime)}

/* call to action */
.cta-text{left:270px;top:2380px;width:660px;text-align:center;font-size:13.5px;line-height:20px;color:var(--muted)}
.cta-call{left:0;top:2440px;width:1200px;display:flex;justify-content:center;align-items:center;gap:10px;font-size:20px;font-family:"Libre Baskerville",Georgia,serif}
.cta-quote{left:522px;top:2488px;width:160px}

/* footer */
.footer-contact{left:0;top:2570px;width:464px;height:366px;background:var(--footer);color:var(--white);padding:38px 0 0 158px}
.footer-contact h2{font-size:20px;margin-bottom:20px}
.footer-contact p{font-size:12px;line-height:18px;margin-bottom:14px}
.footer-contact b{font-weight:700}
.social{display:flex;align-items:center;gap:10px;font-size:12px}
.social i{width:10px;height:10px;border-radius:50%;background:#fff}
.footer-map{left:464px;top:2570px;width:736px;height:366px;background:linear-gradient(90deg,#e6e4e0 0%,#e6e4e0 8%,#b9d8a6 12%,#c6e0b2 20%,#eceae6 24%,#e4e2de 60%,#f0efec 100%)}
.bottom-bar{left:0;top:2936px;width:1200px;height:49px;background:var(--bar);color:#ccc;font-size:11px;display:flex;align-items:center;padding-left:158px}
.to-top{left:1018px;top:2952px;width:24px;height:18px;border:2px solid var(--lime);border-radius:3px}
</style>
</head>
<body>

<header class="site-header">
  <div class="brand">
    <span class="brand-dot"></span>
    <span class="brand-name">ferncliff<small>PHYSICAL THERAPY</small></span>
  </div>
  <nav class="main-nav">
    <a class="active" href="#">Home</a><a href="#">About Us</a><a href="#">Services</a><a href="#">Insurance</a><a href="#">Testimonials</a><a href="#">Contact Us</a>
  </nav>
  <a class="btn btn-lime nav-book" href="#">Book Appointment</a>
</header>

<section>
  <div class="abs hero-photo" role="img" aria-label="Therapist guiding a young patient on a treadmill in a bright clinic gym"></div>
  <div class="abs hero-panel">
    <h1 class="serif">Welcome to Ferncliff Physical Therapy</h1>
    <p>Our therapist owned practice is committed to restoration, wellness and quality of life providing compassionate</p>
    <a class="btn btn-lime hero-contact" href="#">Contact Us</a>
  </div>
  <div class="slider-arrows" style="left:906px;top:528px"><span>«</span><span>»</span></div>
</section>

<section>
  <h2 class="section-title serif" style="left:154px;top:666px">
    <svg width="22" height="60" viewBox="0 0 22 60"><path d="M20 2 A28 28 0 0 0 20 58" fill="none" stroke="var(--teal)" stroke-width="3"/></svg>About Us
  </h2>
  <div class="abs about-text">
    <p>Welcome to Ferncliff Physical Therapy, southeast Denver's choice for healing and rehabilitation. Our therapist owned practice is committed to restoration, wellness and quality of life providing compassionate, skilled care to clients of all ages.</p>
    <p>Ferncliff Physical Therapy treats a wide range of injuries and conditions, whether you're recovering from surgery, returning to athletics or enhancing sports performance. Partnering with you to achieve and maintain a healthy, vigorous lifestyle, our therapists deliver exceptional, progressive care in a comfortable, well-equipped environment.</p>
  </div>
  <a class="btn btn-teal about-more" href="#">Discover More</a>
  <div class="abs about-collage">
    <div role="img" aria-label="Woman relaxing during a massage treatment"></div>
    <div role="img" aria-label="Athlete training with resistance bands"></div>
    <div role="img" aria-label="Pilates reformer exercise"></div>
    <div role="img" aria-label="Exercise ball session with a therapist"></div>
  </div>
</section>

<section class="abs services">
  <h2 class="section-title serif" style="left:154px;top:80px">
    <svg width="22" height="60" viewBox="0 0 22 60"><path d="M20 2 A28 28 0 0 0 20 58" fill="none" stroke="var(--teal)" stroke-width="3"/></svg>What we do?
  </h2>
  <p class="abs services-intro">Manual Therapy/ Soft Tissue Mobilization Laser and Infrared Therapy Custom Orthotics and Foot Evaluations Core Stabilization and Pilates Alignment Training Dry Needling</p>
  <a class="btn btn-teal services-all" href="#">View All</a>
  <article class="service-card" style="left:386px">
    <div class="photo" role="img" aria-label="Massage therapy session" style="background:linear-gradient(170deg,#f7f3ef 0%,#ead7c7 35%,#c99a7a 60%,#3a2c26 80%,#efe8e2 100%)"></div>
    <h3>Massage Therapy</h3><p>There are many variations of passages of Lorem Ipsum available, but the...</p><a href="#">Read More »</a>
  </article>
  <article class="service-card active" style="left:614px">
    <div class="photo" role="img" aria-label="Group pilates class with exercise balls" style="background:linear-gradient(180deg,#7a7470 0%,#c9b4a4 35%,#3b3f44 55%,#b9c0c4 75%,#8e979c 100%)"></div>
    <h3>Pilates</h3><p>There are many variations of passages of Lorem Ipsum available, but the...</p><a href="#">Read More »</a>
  </article>
  <article class="service-card" style="left:844px">
    <div class="photo" role="img" aria-label="Children at football training on a field" style="background:linear-gradient(180deg,#8f9a8a 0%,#7b8b6a 35%,#3a3d40 55%,#6f7f4e 75%,#8a8a56 100%)"></div>
    <h3>Sport Training</h3><p>There are many variations of passages of Lorem Ipsum available, but the...</p><a href="#">Read More »</a>
  </article>
</section>

<section>
  <h2 class="section-title serif" style="left:154px;top:1480px">
    <svg width="22" height="60" viewBox="0 0 22 60"><path d="M20 2 A28 28 0 0 0 20 58" fill="none" stroke="var(--teal)" stroke-width="3"/></svg>Meet Our Providers
  </h2>
  <div class="slider-arrows" style="left:968px;top:1496px"><span>«</span><span>»</span></div>
  <div class="provider" style="left:196px"><div class="avatar" role="img" aria-label="Portrait of Laura Renner" style="background:radial-gradient(circle at 50% 45%,#d9b49a 0%,#8a6550 40%,#3a302b 100%)"></div><h4>Laura Renner</h4><span>PT, Owner</span></div>
  <div class="provider highlight" style="left:406px"><div class="avatar" role="img" aria-label="Portrait of Maya Brandt with profile links"><i></i><i></i><i></i></div><h4>Maya Brandt</h4><span>PT, MS</span></div>
  <div class="provider" style="left:618px"><div class="avatar" role="img" aria-label="Portrait of Sarah Holden" style="background:radial-gradient(circle at 50% 42%,#e9c2a8 0%,#8b5a3e 45%,#e86a8a 80%,#5a4a44 100%)"></div><h4>Sarah Holden</h4><span>DPT, SCS</span></div>
  <div class="provider" style="left:830px"><div class="avatar" role="img" aria-label="Portrait of Stacy Morgan" style="background:radial-gradient(circle at 50% 42%,#f1d2b8 0%,#e6c77a 40%,#d8303a 80%,#6d7174 100%)"></div><h4>Stacy Morgan</h4><span>MPT</span></div>
  <a class="btn btn-teal providers-all" href="#">View All</a>
</section>

<section class="abs testimonials">
  <h2 class="section-title serif" style="left:154px;top:48px">
    <svg width="22" height="60" viewBox="0 0 22 60"><path d="M20 2 A28 28 0 0 0 20 58" fill="none" stroke="var(--teal)" stroke-width="3"/></svg>Testimonials
  </h2>
  <div class="slider-arrows" style="left:968px;top:64px"><span>«</span><span>»</span></div>
  <div class="abs video" role="img" aria-label="Video testimonial from a patient">
    <svg class="abs play" viewBox="0 0 52 52"><circle cx="26" cy="26" r="24" fill="none" stroke="#fff" stroke-width="2"/><path d="M21 16 L36 26 L21 36 Z" fill="none" stroke="#fff" stroke-width="2"/></svg>
  </div>
  <svg class="abs quote-mark" width="48" height="32" viewBox="0 0 48 32"><path d="M2 30 V18 Q2 4 18 2 V8 Q10 10 10 16 H18 V30 Z M28 30 V18 Q28 4 44 2 V8 Q36 10 36 16 H44 V30 Z" fill="var(--lime)"/></svg>
  <p class="abs quote-text">Laura Renner has always provided my patients with extremely efficient and effective therapy that is second to none. My patients that had physical therapy with Laura are consistently very satisfied.</p>
  <p class="abs quote-name">Dana Jennings</p>
  <p class="abs quote-role">MD</p>
  <div class="abs dots"><i></i><i class="on"></i><i></i></div>
</section>

<section>
  <p class="abs cta-text">Contrary to popular belief, Lorem Ipsum is not simply random text. It has roots in a piece of classical Latin literature from 45 BC</p>
  <div class="abs cta-call">
    <svg width="16" height="22" viewBox="0 0 16 22"><rect x="2" y="1" width="12" height="20" rx="2" fill="none" stroke="var(--ink)" stroke-width="2"/><rect x="6" y="16" width="4" height="2" fill="var(--ink)"/></svg>
    <span>Call: 303-555-0142</span>
  </div>
  <a class="btn btn-lime cta-quote" href="#">Request a Quote</a>
</section>

<footer>
  <div class="abs footer-contact">
    <h2 class="serif">Contact Us</h2>
    <p><b>Ferncliff Physical Therapy</b><br>P.O. Box 4410 Parker, CO 80134</p>
    <p><b>Call Us :</b><br>Phone : 303-555-0142<br>Fax : 303-555-0187</p>
    <p><b>Email :</b><br>info@ferncliffpt.net</p>
    <p style="margin-bottom:8px"><b>Follow Us :</b></p>
    <div class="social"><i></i><span>|</span><i></i><span>|</span><i></i></div>
  </div>
  <div class="abs footer-map" role="img" aria-label="Street map showing the clinic location near Parker, Colorado"></div>
  <div class="abs bottom-bar">© 2017 Ferncliff Physical Therapy. All Rights Reserved.</div>
  <div class="abs to-top"></div>
</footer>

</body>
</html>
```